KORVELTA Corporate Business Card

Modern business card design for company which focuses in the areas of Staffing, IT Consulting & Data Services. Please note: We are no longer using the IT subscript on the logo. All designs should have IT subscript removed.
Website: www.korveltait.example

```html
<!DOCTYPE html>
<html lang="en">
<head>
<meta charset="utf-8">
<title>KORVELTA Business Card</title>
<link rel="stylesheet" href="https://fonts.googleapis.com/css2?family=Montserrat:wght@400;600;700&display=swap">
<style>
  :root {
    --stage: #2b2c2e;
    --brand-navy: #0a5b99;
    --brand-sky: #1c96d6;
    --ink: #2a2f38;
    --paper: #ffffff;
    --pattern-tint: #0d629f;
  }
  * { margin: 0; padding: 0; box-sizing: border-box; }
  html, body {
    width: 1200px; height: 900px; overflow: hidden;
    background: var(--stage);
    font-family: "Montserrat", sans-serif;
  }
  .stage { position: relative; width: 1200px; height: 900px; }

  .card {
    position: absolute; left: 260px;
    width: 680px; height: 389px;
    border-radius: 26px; overflow: hidden;
  }
  /* Back side */
  .card-back { top: 40px; background: var(--brand-navy); }
  .card-back .pattern-field {
    position: absolute; inset: 0;
    background: linear-gradient(135deg, var(--pattern-tint), var(--brand-navy));
  }
  .card-back .wordmark {
    position: absolute; right: 60px; bottom: 70px;
    font-weight: 700; font-size: 64px; letter-spacing: 2px;
    color: var(--paper);
  }

  /* Front side */
  .card-front { top: 471px; background: var(--paper); }
  .card-front .swoosh { position: absolute; inset: 0; width: 680px; height: 389px; }
  .brand {
    position: absolute; left: 48px; top: 40px;
    display: flex; align-items: center; gap: 12px;
  }
  .brand-square {
    width: 40px; height: 40px; border-radius: 6px;
    background: var(--brand-sky);
  }
  .brand-name {
    font-weight: 700; font-size: 52px; letter-spacing: 1px;
    color: var(--brand-sky); line-height: 1;
  }
  .accent-bar {
    position: absolute; left: 0; top: 126px;
    width: 12px; height: 40px; background: var(--brand-navy);
  }
  .person {
    position: absolute; left: 60px; top: 122px;
  }
  .person-name {
    font-weight: 700; font-size: 30px; color: var(--brand-sky);
    letter-spacing: 1px;
  }
  .person-title {
    font-size: 19px; color: var(--ink); letter-spacing: 1px; margin-top: 2px;
  }
  .rule {
    width: 170px; height: 2px; background: var(--brand-navy); margin: 8px 0 10px;
  }
  .address, .contact-line {
    font-size: 19px; color: var(--ink); letter-spacing: 1px; line-height: 1.3;
  }
  .contacts { margin-top: 8px; }
  .contact-line { display: flex; align-items: center; gap: 10px; }
  .contact-line svg { width: 16px; height: 16px; flex: none; }
</style>
</head>
<body>
<main class="stage">
  <section class="card card-back">
    <div class="pattern-field" role="img" aria-label="Faint repeating brand-symbol pattern"></div>
    <div class="wordmark">KORVELTA</div>
  </section>

  <section class="card card-front">
    <svg class="swoosh" viewBox="0 0 680 389" aria-hidden="true">
      <rect width="680" height="389" fill="var(--brand-navy)"/>
      <path d="M0 0 H600 C646 62 652 172 610 254 C534 376 200 396 0 344 Z" fill="var(--paper)"/>
      <path d="M0 0 H596 C640 62 646 170 604 250 C530 370 200 390 0 338 Z" fill="var(--brand-sky)"/>
      <path d="M0 0 H580 C620 60 628 162 588 242 C518 358 200 378 0 328 Z" fill="var(--paper)"/>
    </svg>

    <div class="brand">
      <span class="brand-square"></span>
      <span class="brand-name">KORVELTA</span>
    </div>

    <div class="accent-bar"></div>

    <div class="person">
      <div class="person-name">Dorian Vale</div>
      <div class="person-title">Managing Director</div>
      <div class="rule"></div>
      <div class="address">418 Larkspur Ave.<br>Brenton Falls, IN 47900</div>
      <div class="contacts">
        <div class="contact-line">
          <svg viewBox="0 0 16 16"><path d="M4 1 L6 5 L4.5 6.5 C5.5 8.5 7.5 10.5 9.5 11.5 L11 10 L15 12 L13.5 15 C7 14.5 1.5 9 1 2.5 Z" fill="var(--brand-navy)"/></svg>
          <span>555-014-2290</span>
        </div>
        <div class="contact-line">
          <svg viewBox="0 0 16 16"><rect x="1" y="3" width="14" height="10" rx="1" fill="var(--brand-navy)"/><path d="M2 4 L8 9 L14 4" stroke="#fff" stroke-width="1.4" fill="none"/></svg>
          <span>contactus@korveltait.example</span>
        </div>
        <div class="contact-line">
          <svg viewBox="0 0 16 16"><circle cx="8" cy="8" r="7" fill="var(--brand-navy)"/><path d="M1 8 H15 M8 1 C4 5 4 11 8 15 C12 11 12 5 8 1" stroke="#fff" stroke-width="1" fill="none"/></svg>
          <span>www.korveltait.example</span>
        </div>
      </div>
    </div>
  </section>
</main>
</body>
</html>
```